Business card needed for the Vantro of Dry Cleaning!

We need a slick business card design for a new company based out of Montreal called Casiers Pli&Zip inc. (in French) and Pli&Zip Lockers inc. (in English). We're the Vantro of Laundry. We offer services of dry cleaning, laundry (wash&fold), minor clothing alterations, shoe repair and parcel delivery through 24/7 secured and connected lockers. Ordres are placed through our mobile application. Real time notification are sent to customers when their order is ready for pickup. The lockers will be placed throughout the downtown area, in condo and office towers, where a high density of busy people converge. It is simple, user-friendly, and most importantly convenient. We're the out of the box dry cleaner, literally.
Updates

Target Market(s)

1) Professional workers wearing suits daily
2) Campus students living in residences
3) People using laundromats
4) Families with children/yuppies who prefer to use their time doing something else than laundry

Industry/Entity Type

Dry Cleaning

Contact Information for Business Card

Name / Sylvie-Anne Berthiaume
Title / CEO & Founder
Company Name / Casiers Pli&Zip inc. | Pli&Zip Lockers inc.
Website www.plizip.ca

Requirements
Must have
• Text Logo: Pli&Zip - Nettoyeurs 24/7 Cleaners
• Logo on one side and contact info on the other (bilingual)
• Minimalist, pure design
• "We care" for your belongings feeling
• Professional, technological, clean & fresh look
Should not have
• No busy visuals. No rainbow colors.

```html
<!DOCTYPE html>
<html lang="fr">
<head>
<meta charset="utf-8">
<title>Pli&amp;Zip – Business Card</title>
<link href="https://fonts.googleapis.com/css2?family=Questrial&display=swap" rel="stylesheet">
<style>
  :root{
    --bg:#e8eaed;
    --card:#ffffff;
    --ink:#4a4b4f;
    --accent:#4bbcd8;
    --band:#f4f5f6;
  }
  *{margin:0;padding:0;box-sizing:border-box}
  html,body{width:1200px;height:1020px;overflow:hidden}
  body{background:var(--bg);font-family:"Questrial",Arial,sans-serif;color:var(--ink);position:relative}

  .card{position:absolute;width:520px;height:297px;background:var(--card);
        box-shadow:0 4px 14px rgba(0,0,0,.12)}
  .card--front{left:50px;top:200px}
  .card--back{left:630px;top:200px}

  .brand-name{display:block;font-size:50px;line-height:1;color:var(--ink);letter-spacing:0}
  .tagline{display:block;color:var(--accent);font-size:16px;letter-spacing:3px;margin-top:8px}

  .card--front .lockup{position:absolute;left:50%;top:50%;transform:translate(-50%,-50%);text-align:center}
  .card--back .lockup{position:absolute;left:30px;top:116px}
  .card--back .brand-name{font-size:40px}
  .card--back .tagline{font-size:13px;letter-spacing:2.5px;margin-top:7px}

  .contact{position:absolute;left:258px;top:72px}
  .contact__name{font-size:21px;color:var(--ink);letter-spacing:.5px}
  .contact__title{font-size:14px;color:var(--accent);margin:3px 0 12px}
  .contact__row{display:flex;align-items:center;gap:10px;font-size:13.5px;margin-bottom:9px;padding-left:10px}
  .contact__row svg{width:18px;height:14px;flex:none;fill:none;stroke:var(--accent);stroke-width:1.4}

  .variants{position:absolute;left:0;top:760px;width:1200px;height:260px;background:var(--band)}
  .variant{position:absolute}
  .variant .brand-name{font-size:68px}
  .variant--en{left:50px;top:82px}
  .variant--en .tagline{font-size:24px;letter-spacing:6px;margin-top:10px}
  .variant--fr{left:728px;top:58px}
  .variant--fr .eyebrow{display:block;color:var(--accent);font-size:34px;letter-spacing:3px;margin-bottom:8px}
</style>
</head>
<body>
  <section class="card card--front">
    <div class="lockup">
      <span class="brand-name">Pli&amp;Zip</span>
      <span class="tagline">Nettoyeurs 24/7</span>
    </div>
  </section>

  <section class="card card--back">
    <div class="lockup">
      <span class="brand-name">Pli&amp;Zip</span>
      <span class="tagline">Nettoyeurs 24/7</span>
    </div>
    <div class="contact">
      <div class="contact__name">Sylvie-Anne Berthiaume</div>
      <div class="contact__title">Title / CEO &amp; Founder</div>
      <div class="contact__row">
        <svg viewBox="0 0 18 14"><rect x="1" y="1" width="16" height="12"/><path d="M1 1l8 7 8-7"/></svg>
        <span>000 000 0000</span>
      </div>
      <div class="contact__row">
        <svg viewBox="0 0 18 14"><path d="M2 5c0-3 14-3 14 0v1h-4V4H6v2H2z"/><rect x="4" y="7" width="10" height="6"/><circle cx="9" cy="10" r="1.3"/></svg>
        <span>Email@plizip.ca</span>
      </div>
      <div class="contact__row">
        <svg viewBox="0 0 18 14"><circle cx="9" cy="7" r="6"/><ellipse cx="9" cy="7" rx="2.6" ry="6"/><path d="M3 7h12"/></svg>
        <span>www.plizip.ca</span>
      </div>
    </div>
  </section>

  <section class="variants">
    <div class="variant variant--en">
      <span class="brand-name">Pli&amp;Zip</span>
      <span class="tagline">Lockers inc.</span>
    </div>
    <div class="variant variant--fr">
      <span class="eyebrow">Casiers</span>
      <span class="brand-name">Pli&amp;Zip</span>
    </div>
  </section>
</body>
</html>
```